Single Landing Page Redesign - CRO Experts Welcome!

We need our landing page redesigned. We will be giving a lot of weight to conversion optimization so be sure to redesign the landing page with conversion optimization concepts in mind.

This is the landing page that needs to be redesigned:
http://www.pagecrateworks.example/message_board/forum3.html

Here are some ideas that we think could increase conversions in order of priority:

- Show a screenshot of an example forum, linked to the forum's address (http://forums.mindlantern.example/)

- Change the "Get Feedback from Users" feature to "Mobile Friendly (perhaps a picture of an iphone with a mobile version of our forum loaded in it? - mobile version isn't launched yet)

- Mention "Social Sharing" as a feature. (perhaps mention something about content going viral?)

- Additional testimonials:
"Pagecrate Works has been a superb solution for GoldenVow Journeys. Our customers love it-and the customization available is flexible enough to allow us to "brand" the forums so that they fit with our main site. Tech support has been outstanding, with quick & helpful responses to the questions we've had."
Daniel Ferrow
www.goldenvow.example

"Very simple and easy to set up, yet so customizable. It looks like it resides right on our site."
Tobias Wendling
www.pvtrsa.example

- Additional client logo: swiftrail coaches (swiftrail.example) - It would be better if logos are in a horizontal line in gray.

- Benefits of creating a forum (paragraph or bullet points or any other creative way): Running a forum is an excellent way of creating a community. It can be a place for people to discuss issues, share knowledge, and talk about you, your product, or your service. In the long-term, providing a way for your users to be part of a community can prove to be invaluable in terms of search engine optimization, customer satisfaction, customer/visitor retention, brand awareness, customer support, viral promotion, building trust, and creating a new revenue stream.

- Additional info that can be included, which might increase conversions (not mandatory) (can be reworded or changed as needed):
Embed your forum into an existing website in seconds!
Cloud-Based
Secure - Our forums are equipped with security features that make hackers and spammers a thing of the past.

You are welcome to implement your own ideas as well.

Nice landing pages:
http://www.trymeadowly.example/ (I love the big, wide design.)
http://www.quarnix.example/crm/

The physical layout of the page can be changed completely. The existing text and elements of the landing page can be changed completely. None of the existing landing page has to remain the way it is. Be creative and come up with what you think looks best. The existing landing page is only an example of what we currently have.

The PSD of our logo is attached.

We look forward to seeing your mockups!

```html
<!DOCTYPE html>
<html lang="en">
<head>
<meta charset="utf-8">
<title>Pagecrate Works – Create a Powerful Forum</title>
<link rel="stylesheet" href="https://fonts.googleapis.com/css2?family=PT+Sans:ital,wght@0,400;0,700;1,400;1,700&display=swap">
<style>
:root{
  --red:#b40d0d;
  --ink:#3a3a3a;
  --text:#4a4a4a;
  --line:#d6d6d6;
  --blue:#2d5f93;
  --bg:#ffffff;
  --grey-btn:#6f7174;
  --chat:#2e86d6;
}
*{box-sizing:border-box;margin:0;padding:0}
html,body{width:1053px;height:1200px;overflow:hidden;background:var(--bg)}
body{font-family:"PT Sans",sans-serif;color:var(--text);position:relative}
a{text-decoration:none}
.abs{position:absolute}

/* header */
.brand{left:133px;top:12px;display:flex;align-items:center;gap:6px}
.brand-mark{width:52px;height:52px;border-radius:50%;border:5px solid #8aa3bd;background:#eef3f8}
.brand-name{font-size:20px;font-weight:700;color:var(--blue);letter-spacing:-.3px}
.search{left:523px;top:17px;width:158px;height:30px;border:1px solid var(--line);border-radius:3px;background:#fff;display:flex;align-items:center;padding:0 4px 0 8px;justify-content:space-between}
.search-btn{background:#4d7699;color:#fff;font-size:11px;padding:3px 7px;border-radius:2px}
.call{left:701px;top:14px;width:139px;height:36px;background:var(--grey-btn);border-radius:3px;display:flex;align-items:center;gap:8px;padding-left:10px;color:#fff}
.call small{display:block;font-size:10px;line-height:11px}
.call strong{display:block;font-size:13px;font-weight:400;line-height:15px}
.chat{left:846px;top:14px;width:75px;height:36px;background:var(--chat);border-radius:3px;color:#fff;padding:3px 8px}
.chat small{display:block;font-size:8px;line-height:9px}
.chat strong{font-size:13px;line-height:16px}
.nav{right:134px;top:65px;display:flex;font-size:12px}
.nav a{color:var(--blue);padding:0 10px;border-left:1px solid var(--line);line-height:24px}
.nav a:first-child{border-left:0}
.header-rule{left:135px;top:89px;width:786px;height:8px;background:linear-gradient(#e4e6e8,#fff)}

/* hero */
.hero-shot{left:135px;top:120px;width:403px;height:248px;display:block}
.shot-frame{position:absolute;border-radius:10px;background:#1e1e1e;padding:14px 10px}
.shot-screen{width:100%;height:100%;background:linear-gradient(#e8ecf2 0 8%,#fff 8% 14%,#f1f3f6 14%)}
.shot-caption{position:absolute;left:0;bottom:-2px;width:100%;text-align:center;font-size:9px;font-style:italic;color:var(--blue)}
.hero-divider{left:576px;top:128px;width:1px;height:230px;background:#cfcfcf}
.hero-title{left:618px;top:120px;font-size:32px;line-height:40px;font-weight:700;color:var(--ink);letter-spacing:.2px}
.hero-sub{left:618px;top:244px;font-size:19px;line-height:26px;color:var(--red)}
.btn{background:var(--red);color:#fff;font-style:italic;border-radius:3px;display:inline-block;text-align:center}
.hero-btn{left:620px;top:289px;width:66px;height:25px;line-height:25px;font-size:11px;font-weight:700}
.dots{left:621px;top:353px;display:flex;gap:5px}
.dots i{width:12px;height:12px;border-radius:50%;border:1px solid #aaa;background:#fff;display:block}
.dots i.on{background:radial-gradient(#777 35%,#fff 40%)}

/* features */
.board{left:135px;top:400px;width:786px;height:678px;border:1px solid var(--line);box-shadow:0 0 3px rgba(0,0,0,.08)}
.features{display:grid;grid-template-columns:191px 202px 199px 192px;grid-template-rows:175px 178px;border-bottom:1px solid var(--line)}
.feature{border-right:1px solid var(--line);padding:13px 12px 0 12px;position:relative}
.feature:nth-child(4n){border-right:0}
.feature:nth-child(-n+4){border-bottom:1px solid var(--line)}
.feature h3{font-size:14px;font-weight:400;color:var(--red);height:26px}
.feature .icon{position:absolute;right:14px;top:12px}
.feature .pic{width:164px;height:66px;border:1px solid var(--line)}
.feature p{font-size:11px;line-height:16px;margin-top:11px;color:var(--text)}

.cta{left:12px;top:368px;width:438px;height:83px;background:linear-gradient(#fff,#eef0f1);text-align:center;padding-top:14px;font-size:16.5px;line-height:23px;color:var(--red)}
.cta-btn{left:167px;top:439px;width:128px;height:26px;line-height:26px;font-size:15px}
.benefits{left:12px;top:472px;width:441px;text-align:center;font-size:9.5px;line-height:13px;color:var(--text)}
.benefits b{color:var(--red);font-weight:400}
.dotted{left:17px;top:497px;width:437px;border-top:1px dotted #aaa}
.box-head{border:1px solid var(--line);border-radius:2px;height:30px;line-height:29px;padding-left:10px;font-size:14px;color:var(--red)}
.clients-head{left:12px;top:524px;width:441px}
.clients{left:20px;top:576px;width:426px;display:flex;gap:8px;justify-content:center}
.client{height:34px;border:1px solid var(--line);display:flex;align-items:center;justify-content:center;gap:5px;font-size:10px;font-weight:700;color:#7a7a7a;padding:0 6px;white-space:nowrap}
.client i{width:10px;height:10px;background:#9a9a9a;display:block}

.testi-head{left:620px;top:366px;width:0}
.testi{left:482px;width:290px;display:flex;gap:14px}
.avatar{width:41px;height:41px;flex:none}
.testi blockquote{font-size:9.5px;line-height:15.5px;font-style:italic;color:var(--text)}
.testi cite{display:block;color:var(--red);font-size:9.5px;margin-top:4px;line-height:15.5px}
.testi-btn{left:664px;top:637px;width:104px;height:20px;line-height:20px;font-size:10px}

/* footer */
.ribbon{top:1093px;width:104px;height:20px;line-height:20px;padding-left:8px;background:var(--red);color:#fff;font-style:italic;font-size:10px;border-radius:6px}
.social{left:139px;top:1127px;display:flex;gap:7px}
.social i{width:17px;height:17px;border-radius:2px;display:block}
.foot-links{right:130px;top:1131px;font-size:10.5px;font-style:italic;color:var(--text)}
.foot-rule{left:135px;top:1164px;width:786px;border-top:1px solid var(--line)}
.copy{left:0;width:1053px;top:1179px;text-align:center;font-size:10.5px;font-style:italic;color:var(--text)}
</style>
</head>
<body>

<header>
  <div class="abs brand"><span class="brand-mark"></span><span class="brand-name">Pagecrate Works</span></div>
  <div class="abs search">
    <svg width="12" height="12" viewBox="0 0 12 12"><circle cx="5" cy="5" r="3.5" fill="none" stroke="#777" stroke-width="1.5"/><line x1="7.5" y1="7.5" x2="11" y2="11" stroke="#777" stroke-width="1.5"/></svg>
    <span class="search-btn">Search</span>
  </div>
  <div class="abs call">
    <svg width="16" height="22" viewBox="0 0 16 22"><path d="M4 1h3l1 5-2 2c1 3 2 5 4 7l2-1 3 3-2 4C6 19 1 10 2 2z" fill="#fff"/></svg>
    <div><small>Call Us Now</small><strong>1-800-555-0142</strong></div>
  </div>
  <div class="abs chat"><small>Chat to us</small><strong>LIVE!</strong></div>
  <nav class="abs nav"><a href="#">Home</a><a href="#">Features</a><a href="#">Pricing</a><a href="#">Contact Us</a></nav>
  <div class="abs header-rule"></div>
</header>

<section class="hero">
  <a class="abs hero-shot" href="http://forums.mindlantern.example/" role="img" aria-label="Screenshot of an example forum at forums.mindlantern.example shown on two tablets">
    <span class="shot-frame" style="left:0;top:0;width:238px;height:232px"><span class="shot-screen" style="display:block"></span></span>
    <span class="shot-frame" style="left:245px;top:50px;width:158px;height:182px;transform:skewY(-4deg)"><span class="shot-screen" style="display:block;background:linear-gradient(#c41a1a 0 6%,#fff 6% 12%,#f3f3f3 12%)"></span></span>
    <span class="shot-caption">See an example forum: forums.mindlantern.example</span>
  </a>
  <div class="abs hero-divider"></div>
  <h1 class="abs hero-title">THE EASIEST WAY<br>TO CREATE A<br>POWERFUL FORUM</h1>
  <p class="abs hero-sub">No Coding, Software, or Servers!</p>
  <a class="abs btn hero-btn">Read More</a>
  <div class="abs dots"><i></i><i class="on"></i><i></i><i></i><i></i></div>
</section>

<main class="abs board">
  <div class="features">
    <div class="feature"><h3>Instant Setup</h3>
      <svg class="icon" width="22" height="24" viewBox="0 0 22 24"><circle cx="11" cy="14" r="9" fill="none" stroke="#b8b8b8" stroke-width="2"/><rect x="9" y="1" width="4" height="3" fill="#b8b8b8"/><line x1="11" y1="14" x2="11" y2="8" stroke="#b8b8b8" stroke-width="2"/></svg>
      <div class="pic" role="img" aria-label="Businessman on the phone at his desk" style="background:linear-gradient(#d8d8d8,#9a9ea4)"></div><p>Embed your forum into an existing website in seconds. You'll be up and running right away!</p></div>
    <div class="feature"><h3>Fully Customizable</h3>
      <svg class="icon" width="26" height="22" viewBox="0 0 26 22"><path d="M13 2 3 20h20z" fill="none" stroke="#b8b8b8" stroke-width="2"/><line x1="6" y1="14" x2="20" y2="14" stroke="#b8b8b8" stroke-width="2"/></svg>
      <div class="pic" role="img" aria-label="Forum theme shown on several screens" style="background:linear-gradient(#2b2b2b,#5a6a4a)"></div><p>Customize every aspect of your forum, including the design and features.</p></div>
    <div class="feature"><h3>Social Sharing</h3>
      <svg class="icon" width="24" height="22" viewBox="0 0 24 22"><circle cx="5" cy="11" r="3.5" fill="#b8b8b8"/><circle cx="19" cy="4" r="3.5" fill="#b8b8b8"/><circle cx="19" cy="18" r="3.5" fill="#b8b8b8"/><path d="M5 11 19 4M5 11l14 7" stroke="#b8b8b8" stroke-width="2"/></svg>
      <div class="pic" role="img" aria-label="Crowd of people sharing content at an event" style="background:linear-gradient(#6a5e58,#3a3430)"></div><p>One-click sharing lets members spread great threads, so your content can go viral.</p></div>
    <div class="feature"><h3>Mobile Friendly</h3>
      <svg class="icon" width="16" height="24" viewBox="0 0 16 24"><rect x="1" y="1" width="14" height="22" rx="2" fill="none" stroke="#b8b8b8" stroke-width="2"/><circle cx="8" cy="19" r="1.5" fill="#b8b8b8"/></svg>
      <div class="pic" role="img" aria-label="Smartphone showing the mobile version of a forum" style="background:linear-gradient(#eadfd6,#c9b7ab)"></div><p>A mobile version of your forum lets members read and post from any smartphone.</p></div>
    <div class="feature"><h3>White Label</h3>
      <svg class="icon" width="20" height="24" viewBox="0 0 20 24"><line x1="3" y1="2" x2="3" y2="23" stroke="#b8b8b8" stroke-width="2"/><path d="M4 3h14l-4 5 4 5H4z" fill="#b8b8b8"/></svg>
      <div class="pic" role="img" aria-label="Domain name signs" style="background:linear-gradient(90deg,#2a78c8,#3aa04a,#c8302a)"></div><p>Use your own logo and domain name. Pagecrate Works is completely invisible to your users!</p></div>
    <div class="feature"><h3>Fanatic Support</h3>
      <svg class="icon" width="24" height="24" viewBox="0 0 24 24"><circle cx="12" cy="12" r="10" fill="none" stroke="#b8b8b8" stroke-width="4"/><circle cx="12" cy="12" r="4" fill="#fff"/></svg>
      <div class="pic" role="img" aria-label="Support agent with headset" style="background:linear-gradient(90deg,#5a3a2a,#c9c9c9)"></div><p>Industry-leading phone, chat, and email support.</p></div>
    <div class="feature"><h3>SEO Friendly</h3>
      <svg class="icon" width="24" height="24" viewBox="0 0 24 24"><circle cx="9" cy="9" r="6.5" fill="none" stroke="#b8b8b8" stroke-width="3"/><line x1="14" y1="14" x2="22" y2="22" stroke="#b8b8b8" stroke-width="4"/></svg>
      <div class="pic" role="img" aria-label="Hand holding a search optimization sphere" style="background:radial-gradient(circle,#e8d64a 10%,#f4f4f4 45%)"></div><p>Search Engine Optimization is built into the foundation, driving more traffic to your forum.</p></div>
    <div class="feature"><h3>Secure &amp; Moderated</h3>
      <svg class="icon" width="20" height="24" viewBox="0 0 20 24"><path d="M10 1 2 4v7c0 6 4 10 8 12 4-2 8-6 8-12V4z" fill="#b8b8b8"/></svg>
      <div class="pic" role="img" aria-label="Woman working at a laptop" style="background:linear-gradient(90deg,#c04a7a,#d8d8e0)"></div><p>Cloud-based security keeps hackers and spammers out. Approve posts before they go live.</p></div>
  </div>

  <div class="abs cta">Pagecrate Works proudly serves over 100 million visits<br>per month to over 15,000 forums...</div>
  <a class="abs btn cta-btn">Create A Forum Now</a>
  <p class="abs benefits">A forum builds a community that boosts <b>SEO</b>, <b>retention</b>, <b>brand awareness</b>,<br><b>customer support</b>, <b>viral promotion</b>, <b>trust</b> and a <b>new revenue stream</b>.</p>
  <div class="abs dotted"></div>
  <div class="abs box-head clients-head">Featured Clients</div>
  <div class="abs clients">
    <div class="client"><i></i>Harbor Aid</div>
    <div class="client">Norvanta</div>
    <div class="client">Elmridge University</div>
    <div class="client">Frostel Creamery</div>
    <div class="client">Swiftrail</div>
  </div>

  <div class="abs box-head" style="left:478px;top:366px;width:294px">Testimonials</div>
  <div class="abs testi" style="top:412px">
    <div class="avatar" role="img" aria-label="Portrait of Daniel Ferrow" style="background:#5a4a44"></div>
    <div><blockquote>"Pagecrate Works has been a superb solution for GoldenVow Journeys. Our customers love it-and the customization available is flexible enough to allow us to "brand" the forums so that they fit with our main site. Tech support has been outstanding, with quick &amp; helpful responses to the questions we've had."</blockquote><cite>Daniel Ferrow<br>www.goldenvow.example</cite></div>
  </div>
  <div class="abs" style="left:488px;top:545px;width:280px;border-top:1px dotted #aaa"></div>
  <div class="abs testi" style="top:558px">
    <div class="avatar" role="img" aria-label="Portrait of Tobias Wendling" style="background:#4a4440"></div>
    <div><blockquote>"Very simple and easy to set up, yet so customizable. It looks like it resides right on our site."</blockquote><cite>Tobias Wendling<br>www.pvtrsa.example</cite></div>
  </div>
  <a class="abs btn testi-btn">Read All Testimonials</a>
</main>

<footer>
  <div class="abs ribbon" style="left:137px">Follow Us On</div>
  <div class="abs ribbon" style="left:818px">Links</div>
  <div class="abs social"><i style="background:#3b5a9a"></i><i style="background:#e8731c"></i><i style="background:#33a3dc"></i><i style="background:#1a6ca8"></i></div>
  <div class="abs foot-links">Home &nbsp; / &nbsp;Features &nbsp;/ &nbsp;Pricing &nbsp;/ &nbsp;Contact Us</div>
  <div class="abs foot-rule"></div>
  <div class="abs copy">Copyrights @ 2013 All Rights Reserved</div>
</footer>

</body>
</html>
```